Brightmere email header for parts

We sell parts to the construction equipment industry. We want a header for our emails that reflect what we do. I will include what we have now but want something for parts only. Added a lot of pictures just so you can look through what we do.

```html
<!DOCTYPE html>
<html lang="en">
<head>
<meta charset="utf-8">
<title>Brightmere – Parts Solutions Email Header</title>
<link rel="stylesheet" href="https://fonts.googleapis.com/css2?family=Oswald:wght@400;500;700&display=swap">
<style>
  :root {
    --brand-red: #c61f2d;
    --white: #ffffff;
    --steel-dark: #4a4a48;
    --steel-mid: #9a9a98;
    --steel-light: #d6d6d4;
    --machine-yellow: #e8b416;
    --machine-amber: #c78f0c;
  }
  html, body {
    margin: 0;
    padding: 0;
    overflow: hidden;
    background: var(--white);
  }
  .header {
    position: relative;
    width: 1200px;
    height: 343px;
    background: var(--brand-red);
    overflow: hidden;
    font-family: "Oswald", "Arial Narrow", sans-serif;
    color: var(--white);
  }
  .header__art {
    position: absolute;
    inset: 0;
    width: 1200px;
    height: 343px;
  }
  .brand {
    position: absolute;
    left: 24px;
    top: 148px;
    width: 280px;
  }
  .brand__mark {
    display: block;
    width: 22px;
    height: 22px;
    background: var(--white);
    margin-bottom: 10px;
  }
  .brand__name {
    margin: 0;
    font-weight: 700;
    font-size: 44px;
    line-height: 1;
    letter-spacing: 1px;
    text-transform: uppercase;
  }
  .brand__rule {
    height: 5px;
    width: 262px;
    background: var(--white);
    margin-top: 6px;
  }
  .contact__email {
    margin: 10px 0 0;
    font-weight: 400;
    font-size: 17px;
    letter-spacing: 0.3px;
  }
  .contact__phone {
    margin: 4px 0 0;
    font-weight: 500;
    font-size: 46px;
    line-height: 1.05;
    letter-spacing: 1px;
  }
  .headline {
    position: absolute;
    left: 328px;
    top: 18px;
    margin: 0;
    font-weight: 700;
    font-size: 76px;
    line-height: 1.1;
    letter-spacing: 1.5px;
    text-transform: uppercase;
  }
  .services {
    position: absolute;
    left: 330px;
    top: 110px;
    margin: 0;
    font-weight: 500;
    font-size: 23px;
    letter-spacing: 0.3px;
  }
</style>
</head>
<body>
  <div class="header">
    <svg class="header__art" viewBox="0 0 1200 343" xmlns="http://www.w3.org/2000/svg">
      <defs>
        <linearGradient id="grad-transmission" x1="0" y1="0" x2="1" y2="1">
          <stop offset="0" stop-color="#6a6660"/>
          <stop offset="0.5" stop-color="#d9a514"/>
          <stop offset="1" stop-color="#3e3c38"/>
        </linearGradient>
        <linearGradient id="grad-sprocket" x1="0" y1="0" x2="0" y2="1">
          <stop offset="0" stop-color="#c9c9c7"/>
          <stop offset="1" stop-color="#8c8c8a"/>
        </linearGradient>
        <linearGradient id="grad-housing" x1="0" y1="0" x2="1" y2="0">
          <stop offset="0" stop-color="#b7b7b5"/>
          <stop offset="0.5" stop-color="#d7a51a"/>
          <stop offset="1" stop-color="#a9a9a7"/>
        </linearGradient>
        <linearGradient id="grad-camshafts" x1="0" y1="0" x2="1" y2="1">
          <stop offset="0" stop-color="#8d8c88"/>
          <stop offset="0.5" stop-color="#3a3a38"/>
          <stop offset="1" stop-color="#6b6a66"/>
        </linearGradient>
        <linearGradient id="grad-yoke" x1="0" y1="0" x2="1" y2="0">
          <stop offset="0" stop-color="#9a9894"/>
          <stop offset="1" stop-color="#e8b416"/>
        </linearGradient>
      </defs>

      <g role="img" aria-label="Photo of a reconditioned yellow transmission on a workshop floor">
        <polygon points="334,158 497,158 412,343 334,343" fill="url(#grad-transmission)"/>
      </g>
      <g role="img" aria-label="Photo of a track sprocket and rollers">
        <polygon points="497,158 592,343 412,343" fill="url(#grad-sprocket)"/>
      </g>
      <g role="img" aria-label="Photo of a yellow gear housing">
        <polygon points="497,158 833,158 695,343 592,343" fill="url(#grad-housing)"/>
      </g>
      <g role="img" aria-label="Photo of camshafts and sprocket segments laid on a pallet">
        <polygon points="695,343 951,0 1200,0 1200,343" fill="url(#grad-camshafts)"/>
      </g>
      <g role="img" aria-label="Photo of a yellow yoke part">
        <polygon points="1045,0 1200,0 1200,250" fill="url(#grad-yoke)"/>
      </g>

      <polygon points="951,0 1045,0 1000,70" fill="var(--brand-red)"/>

      <g stroke="var(--white)" stroke-width="4" fill="none">
        <line x1="497" y1="158" x2="412" y2="343"/>
        <line x1="497" y1="158" x2="592" y2="343"/>
        <line x1="833" y1="158" x2="695" y2="343"/>
        <line x1="951" y1="0" x2="1000" y2="70"/>
        <line x1="1045" y1="0" x2="1200" y2="250"/>
        <line x1="1045" y1="0" x2="1000" y2="70"/>
      </g>
    </svg>

    <div class="brand">
      <span class="brand__mark"></span>
      <p class="brand__name">Brightmere</p>
      <div class="brand__rule"></div>
      <p class="contact__email">jmarlow@brightmereparts.com</p>
      <p class="contact__phone">555 014 2290</p>
    </div>

    <h1 class="headline">Parts Solutions</h1>
    <p class="services">New | Reconditioned | Aftermarket | Used Parts</p>
  </div>
</body>
</html>
```